Philadelphia-based Nonprofit Needs Invitation Design for 11th Annual Cook-Off Fundraiser

Venture Guild (VG) is a non-profit 501(c)(3) microenterprise development organization focused on growing businesses and jobs in our local communities. By connecting hundreds of entrepreneurs each year with access to capital, one-on-one technical assistance, business training and networking opportunities, Venture Guild helps promising individuals to develop economic self-sufficiency and create job opportunities through business ownership.

The theme for our 11th annual Plate of Promise cook-off fundraiser, “Tastes from Around the World: Savor the Flavors,” reflects our commitment to fostering and celebrating the diverse network of entrepreneurs, business owners, and supporters that make VG’s work possible.

Plate of Promise is a chance for Venture Guild to showcase the culinary talents of our entrepreneurs and business owners, while also hosting a fun-filled night with celebrity guest judges, delicious hors d'oeuvres and desserts, a silent auction, and an exciting cook-off contest.

We would like a double-sided, two-color folded invitation (fold size: 5" x 7"); a double-sided, two-color reply card (5” x 4”); a mailing envelope (A7 envelope, grayscale) and a reply envelope (A2 envelope, grayscale). For an example of the design that was on the cover of last year's invitation, see here: http://www.myventureguild.example/sites/vg.relaybureau.example/files/imagecache/250px_thumb/signature_images/VG_HearthsideWarmth.png.

The final design should appeal to a broad range of potential attendees and be inviting and warm. While we send out a different invitation for each Plate of Promise fundraiser, we were very pleased with last year’s invitation (attached, “Plate of Promise Invitation_2011”) and would like an invitation design that is similar (for color scheme please refer to the web link in the above paragraph). A scanned copy of the reply card is also attached ("Plate of Promise Reply Cards 2011"). Finally a copy of the outer envelope is attached ("Plate of Promise Outer Envelope_2011").

Target Market(s)

Our target market includes: existing and past donors; local business owners; and entrepreneurs.

Industry/Entity Type

Non-Profit

Requirements
Must have
• - The main illustration on the invitation should be food-themed
- The invitation should include all of the copy in the attached word .doc ("Plate of Promise Invitation Copy_2013").
Should not have
• - Any designs, backgrounds or fonts that make the invitation difficult to read or understand

```html
<!DOCTYPE html>
<html lang="en">
<head>
<meta charset="utf-8">
<title>Plate of Promise — Reply Card</title>
<link href="https://fonts.googleapis.com/css2?family=Libre+Baskerville:wght@400;700&family=PT+Sans&display=swap" rel="stylesheet">
<style>
  :root {
    --card-red: #b22e26;
    --ink: #1f1b1a;
    --paper: #ffffff;
    --accent-blue: #6b7fb5;
    --backdrop: #ece8e4;
  }
  * { margin: 0; padding: 0; box-sizing: border-box; }
  html, body { width: 1200px; height: 1000px; overflow: hidden; }
  body { background: var(--backdrop); position: relative; }

  .reply-front {
    position: absolute; left: 62px; top: 148px; width: 568px; height: 454px;
    background: var(--card-red); overflow: hidden; z-index: 2;
    font-family: "Libre Baskerville", Georgia, serif;
  }
  .greeting-line {
    position: absolute; white-space: nowrap; color: var(--paper);
    line-height: 1;
  }
  .greeting-line--we-look { left: -4px; top: -33px; font-size: 158px; letter-spacing: -0.05em; }
  .greeting-line--forward { left: -2px; top: 86px; font-size: 148px; letter-spacing: -0.05em; }
  .greeting-line--to-seeing { left: 108px; top: 208px; font-size: 80px; letter-spacing: -0.03em; }
  .greeting-line--you {
    left: 30px; top: 279px; font-size: 205px; color: var(--ink); letter-spacing: -0.06em;
  }
  .greeting-bang {
    position: absolute; left: 496px; top: 272px; font-size: 212px; line-height: 1;
    color: var(--accent-blue);
  }

  .reply-back {
    position: absolute; left: 540px; top: 413px; width: 567px; height: 453px;
    background: var(--paper); overflow: hidden; z-index: 1;
    font-family: "PT Sans", Arial, sans-serif;
  }
  .tickets-heading {
    position: absolute; left: 128px; top: -17px; font-weight: 400;
    color: var(--card-red); font-size: 92px; line-height: 1; letter-spacing: -0.01em;
  }
  .ticket-tier {
    position: absolute; left: 0; width: 100%; text-align: center;
    font-size: 31px; line-height: 1; white-space: nowrap;
  }
  .ticket-tier__name { font-family: "Libre Baskerville", Georgia, serif; color: var(--ink); letter-spacing: -0.03em; font-size: 29px; }
  .ticket-tier__price { color: var(--card-red); }
  .ticket-tier--individual { top: 92px; }
  .ticket-tier--client { top: 175px; }
  .ticket-count {
    position: absolute; left: 162px; display: flex; align-items: center; gap: 4px;
    font-size: 19px; color: var(--ink); letter-spacing: -0.02em;
  }
  .ticket-count__label { display: inline-block; width: 162px; white-space: nowrap; }
  .ticket-count--individual { top: 130px; }
  .ticket-count--client { top: 214px; }
  .ticket-count__box {
    width: 75px; height: 35px; border: 2px solid var(--card-red); border-radius: 2px;
  }
  .name-band {
    position: absolute; left: 0; top: 275px; width: 100%; height: 178px; background: var(--card-red);
  }
  .name-band__label {
    position: absolute; left: 0; width: 100%; top: 12px; text-align: center;
    font-size: 31px; color: var(--ink);
  }
  .name-band__field {
    position: absolute; left: 84px; top: 54px; width: 400px; height: 44px; background: var(--paper);
  }
</style>
</head>
<body>
  <section class="reply-front" aria-label="Reply card front">
    <div class="greeting-line greeting-line--we-look">we look</div>
    <div class="greeting-line greeting-line--forward">forward</div>
    <div class="greeting-line greeting-line--to-seeing">to seeing</div>
    <div class="greeting-line greeting-line--you">YOU</div>
    <div class="greeting-bang">!</div>
  </section>

  <section class="reply-back" aria-label="Reply card back">
    <h1 class="tickets-heading">TICKETS</h1>
    <p class="ticket-tier ticket-tier--individual"><span class="ticket-tier__name">Individual</span> <span class="ticket-tier__price">$75/Ticket</span></p>
    <div class="ticket-count ticket-count--individual"><span class="ticket-count__label">Number of Tickets:</span><span class="ticket-count__box"></span></div>
    <p class="ticket-tier ticket-tier--client"><span class="ticket-tier__name">VG Client</span> <span class="ticket-tier__price">$30/Ticket</span></p>
    <div class="ticket-count ticket-count--client"><span class="ticket-count__label">Number of Tickets:</span><span class="ticket-count__box"></span></div>
    <div class="name-band">
      <p class="name-band__label">Name:</p>
      <div class="name-band__field"></div>
    </div>
  </section>
</body>
</html>
```